Donation Brochure for Ashgrove Meadow Hospital Foundation

We are the Ashgrove Meadow Hospital Foundation in Montreal, Quebec, Canada

We need a brochure that people can fill out in order to make a donation to the Foundation.

The brochure NEEDS TO BE BILINGUAL (English and French) and include a return envelope that can be ripped off from the main brochure, and then sealed with the donation inside.

Please no pictures of buildings, only people.

I have uploaded files to show which fields must be present for donors to fill out.

Target Market(s)

Most of our donors are over the age of 60. 70% Anglophone, 30% Francophone

Industry/Entity Type

Hospital

Requirements
Must have
• Our logo (included in files)

contact info for foundation:

342 Birchwell Ave East, B3.12
Montreal, QC H2K 4B7
Tel: 514-726-3908
Fax: 514-726-3951
email: hope@ashmeadfdn.org
web: ashmeadfdn.org

Return envelope

BILINGUAL
Should not have
• Pictures of buildings

```html
<!DOCTYPE html>
<html lang="en">
<head>
<meta charset="utf-8">
<title>Donation Form / Formulaire de don – Ashgrove Meadow Hospital Foundation</title>
<link rel="stylesheet" href="https://fonts.googleapis.com/css2?family=Roboto+Condensed:ital,wght@0,400;0,700;1,400;1,700&display=swap">
<style>
  :root {
    --page-bg: #e4e4e6;
    --paper: #ffffff;
    --paper-shade: #f1f1f3;
    --navy: #1d2d78;
    --ink: #1b1b1b;
    --muted: #4a4a4a;
    --rule: #333333;
    --blue-top: #2a63b3;
    --blue-bottom: #1f4a8c;
    --gold: #c9a54c;
    --gold-light: #e8d28e;
    --khaki: #d7d39c;
    --field: #eceacb;
  }
  * { box-sizing: border-box; margin: 0; padding: 0; }
  html, body { width: 1200px; height: 1080px; overflow: hidden; }
  body {
    background: var(--page-bg);
    font-family: "Roboto Condensed", "Arial Narrow", sans-serif;
    color: var(--ink);
  }
  .brochure {
    position: absolute; left: 60px; top: 60px;
    width: 1080px; height: 960px;
    display: flex;
    box-shadow: 0 6px 24px rgba(0,0,0,.18);
  }
  .panel { width: 360px; height: 960px; position: relative; background: var(--paper); }
  .en { color: var(--muted); font-style: italic; }

  /* Cover panel */
  .cover { display: flex; flex-direction: column; }
  .photo-hero { height: 270px; background: linear-gradient(180deg, #a9c3dc 0%, #c9d6d8 40%, #8fae7a 75%, #6f9360 100%); }
  .gold-band { height: 10px; background: linear-gradient(90deg, var(--gold), var(--gold-light), var(--gold)); }
  .intro {
    flex: 1;
    background: linear-gradient(180deg, var(--blue-top), var(--blue-bottom));
    color: #fff;
    padding: 20px 20px 0 20px;
    font-size: 15px; line-height: 1.32;
    text-align: justify;
  }
  .intro p + p { margin-top: 12px; }
  .return-envelope {
    margin-top: 16px;
    border: 1.5px dashed rgba(255,255,255,.8);
    padding: 9px 12px;
    font-size: 12px; line-height: 1.35;
    text-align: left;
  }
  .return-envelope .env-title { font-weight: 700; font-size: 13.5px; color: var(--gold-light); }
  .return-envelope .env-note { margin: 2px 0 5px; font-style: italic; }
  .photo-row { height: 190px; display: flex; }
  .photo-patient { width: 50%; background: linear-gradient(180deg, #c8d6e4 0%, #d9c7b0 55%, #9a8a74 100%); border-right: 3px solid var(--gold); }
  .photo-room { width: 50%; background: linear-gradient(160deg, #d9c9a8 0%, #b8a98a 45%, #7e9a6e 100%); }

  /* Tear-off perforation between cover and form */
  .perforation {
    position: absolute; left: 0; top: 0; bottom: 0; width: 0;
    border-left: 2px dashed #8a8a8a;
  }
  .perforation-label {
    position: absolute; left: 6px; top: 470px;
    writing-mode: vertical-rl; transform: rotate(180deg);
    font-size: 9.5px; color: #777; letter-spacing: .5px;
  }

  /* Form panel */
  .form-panel { background: linear-gradient(90deg, var(--paper-shade), var(--paper) 40%); padding: 18px 22px 0 26px; font-size: 12px; }
  .form-title { text-align: center; color: var(--navy); font-weight: 700; font-size: 19px; letter-spacing: .3px; }
  .form-title .en { color: var(--navy); font-weight: 400; font-size: 15px; }
  .form-address { text-align: center; font-weight: 700; font-size: 12px; margin-top: 4px; }
  .section-head { color: var(--navy); font-weight: 700; font-style: italic; font-size: 13px; }
  .section-head .en { color: var(--navy); font-weight: 400; }
  .dedication { margin-top: 16px; }
  .check { display: flex; align-items: center; gap: 5px; margin-top: 2px; }
  .box { width: 9px; height: 9px; border: 1.5px solid var(--ink); flex: none; display: inline-block; }
  .field { display: flex; align-items: flex-end; gap: 4px; margin-top: 13px; white-space: nowrap; }
  .field .line { flex: 1; border-bottom: 1px solid var(--rule); height: 12px; }
  .field .line.short { flex: 0 0 50px; }
  .tax-note { font-size: 9.5px; margin-top: 10px; line-height: 1.25; }
  .payment { background: var(--khaki); margin: 8px -4px 0 -4px; padding: 7px 10px 8px 10px; }
  .payment-title { text-align: center; color: var(--navy); font-size: 12px; }
  .payment-title .en { color: var(--navy); }
  .amount-row { display: flex; align-items: center; gap: 8px; margin-top: 8px; }
  .amount-field { width: 62px; height: 20px; padding: 2px 4px; background: var(--field); }
  .cards { display: flex; gap: 10px; margin-top: 9px; font-size: 12px; }
  .cards .check { margin: 0; gap: 3px; }
  .card-line { border-bottom: 1px solid var(--rule); height: 18px; }
  .small-label { font-size: 11px; margin-top: 2px; }
  .dash-line { font-size: 12px; letter-spacing: 2px; margin-top: 4px; white-space: nowrap; overflow: hidden; }
  .exp-row { display: flex; gap: 16px; font-size: 11px; border-top: 1px solid var(--rule); padding-top: 2px; }
  .reg { font-size: 11.5px; margin-top: 9px; }
  .monthly { margin-top: 13px; }
  .monthly p { line-height: 1.25; }
  .monthly .amount-row { margin-top: 8px; }
  .opts { margin-top: 8px; line-height: 1.25; }
  .opts .check { margin-top: 1px; align-items: flex-start; }
  .opts .check .box { margin-top: 3px; }
  .indent { padding-left: 14px; }
  .guarantee { font-size: 10.5px; margin-top: 8px; line-height: 1.25; }

  /* Tribute panel */
  .tribute-panel { background: linear-gradient(90deg, #f6f6f8, var(--paper) 30%); padding: 34px 26px 0 22px; font-size: 12px; }
  .tribute-intro { text-align: center; color: var(--navy); font-style: italic; font-size: 20px; line-height: 1.3; }
  .tribute-intro .sub { font-size: 15px; }
  .tribute-head { text-align: center; color: var(--navy); font-style: italic; font-size: 20px; margin-top: 22px; }
  .name-line { border-bottom: 1px solid var(--rule); height: 30px; margin-right: 6px; }
  .name-label { margin-top: 3px; }
  .notify { text-align: center; margin-top: 12px; }
  .flourish { height: 6px; width: 140px; margin: 22px auto 0; background: var(--gold); border-radius: 3px; opacity: .85; }
  .anon { margin-top: 34px; display: flex; gap: 4px; align-items: flex-start; font-size: 11.5px; line-height: 1.25; }
  .anon .box { margin-top: 3px; }
  .lang { display: flex; gap: 12px; margin-top: 10px; font-size: 11px; align-items: center; }
  .lang .check { margin: 0; gap: 3px; }
</style>
</head>
<body>
<main class="brochure">

  <section class="panel cover">
    <div class="photo-hero" role="img" aria-label="Photo of a nurse caring for a smiling senior patient"></div>
    <div class="gold-band"></div>
    <div class="intro">
      <p>Every day, the Ashgrove Meadow Hospital Foundation helps our doctors, nurses and staff give patients the best care possible. Your gift funds modern equipment, research and comfort for families across Montreal.</p>
      <p>Chaque jour, la Fondation de l'Hôpital Ashgrove Meadow aide nos médecins, infirmières et employés à offrir les meilleurs soins. Votre don finance l'équipement, la recherche et le confort des familles.</p>
      <div class="return-envelope">
        <p class="env-title">Enveloppe-réponse · Return envelope</p>
        <p class="env-note">Détachez, insérez votre don et scellez.<br>Tear off, insert your gift and seal.</p>
        <p><b>Ashgrove Meadow Hospital Foundation</b><br>342 Birchwell Ave East, B3.12<br>Montreal, QC H2K 4B7<br>Tel: 514-726-3908 · Fax: 514-726-3951<br>hope@ashmeadfdn.org · ashmeadfdn.org</p>
      </div>
    </div>
    <div class="gold-band"></div>
    <div class="photo-row">
      <div class="photo-patient" role="img" aria-label="Photo of a volunteer holding a patient's hand"></div>
      <div class="photo-room" role="img" aria-label="Photo of a family visiting a patient"></div>
    </div>
  </section>

  <section class="panel form-panel">
    <div class="perforation"></div>
    <p class="perforation-label">Détachez ici · Tear here</p>
    <h1 class="form-title">FORMULAIRE DE DON <span class="en">/ DONATION FORM</span></h1>
    <p class="form-address">342 avenue Birchwell E. B3.12, Montréal, Québec, H2K 4B7</p>

    <div class="dedication">
      <p class="section-head">J'aimerais que mon don soit dédié: <span class="en">/ Please direct my gift to:</span></p>
      <p class="check"><span class="box"></span><b>aux Besoins prioritaires</b>&nbsp;<span class="en">/ Priority needs</span></p>
      <div class="check"><span class="box"></span><b>autres:</b>&nbsp;<span class="en">/ Other:</span><span style="flex:1;border-bottom:1px solid var(--rule);height:10px;margin-right:20px"></span></div>
    </div>

    <div class="field">Nom <span class="en">/ Name</span>:<span class="line"></span></div>
    <div class="field">Adresse <span class="en">/ Address</span>:<span class="line"></span>App. <span class="en">/ Apt.</span>:<span class="line short"></span></div>
    <div class="field">Ville <span class="en">/ City</span>:<span class="line"></span></div>
    <div class="field">Province:<span class="line short"></span>Code postal <span class="en">/ Postal code</span>:<span class="line short"></span></div>
    <div class="field">Courriel <span class="en">/ Email</span>:<span class="line"></span></div>
    <div class="field">Tél. domicile <span class="en">/ Home phone</span>:<span class="line"></span></div>
    <div class="field">Tél. cellulaire <span class="en">/ Cell phone</span>:<span class="line"></span></div>
    <p class="tax-note">Un reçu d'impôt sera émis pour tout don avec adresse complète. / A tax receipt will be issued for any gift with a full address.</p>

    <div class="payment">
      <p class="payment-title">MODE DE PAIEMENT <span class="en">/ PAYMENT METHOD</span></p>
      <div class="amount-row">J'aimerais donner <span class="en">/ My gift</span> : <span class="amount-field">$</span></div>
      <p class="check" style="margin-top:8px"><span class="box"></span>Chèque à l'ordre de la Fondation de l'HAM <span class="en">/ Cheque</span></p>
      <div class="cards">
        <span class="check"><span class="box"></span>Carte Nova</span>
        <span class="check"><span class="box"></span>Carte Orbis</span>
        <span class="check"><span class="box"></span>Carte Lumen</span>
      </div>
      <div class="card-line"></div>
      <p class="small-label">Titulaire de la carte <span class="en">/ Cardholder</span></p>
      <p class="dash-line">_ _ _ _&nbsp;&nbsp;_ _ _ _&nbsp;&nbsp;_ _ _ _&nbsp;&nbsp;_ _ _ _</p>
      <p class="small-label">No de carte <span class="en">/ Card number</span></p>
      <p class="dash-line">_ _ / _ _</p>
      <div class="exp-row"><span>Date d'exp. <span class="en">/ Expiry</span></span><span>Signature</span></div>
    </div>

    <p class="reg">No d'enregistrement <span class="en">/ Registration no.</span>: 20457 3381 RR 0001</p>

    <div class="monthly">
      <p class="section-head">Programme de dons mensuels <span class="en">/ Monthly giving</span></p>
      <p>Oui – J'aimerais faire partie des <i>Amis de l'Ashgrove</i>. <span class="en">/ Yes – I would like to give monthly.</span></p>
      <div class="amount-row">Montant mensuel <span class="en">/ Monthly amount</span> : <span class="amount-field">$</span></div>
      <div class="opts">
        <p class="check"><span class="box"></span><span>Je joins un chèque avec la mention NUL. <span class="en">/ Void cheque enclosed.</span></span></p>
        <p class="check"><span class="box"></span><span>J'ai fourni ma carte de crédit plus haut. <span class="en">/ Card given above.</span></span></p>
        <p class="indent">Veuillez percevoir mon don <span class="en">/ Please debit my gift</span></p>
        <p class="check"><span class="box"></span>le 1er ou <span class="box"></span>le 15 de chaque mois <span class="en">/ on the 1st or 15th</span></p>
      </div>
      <p class="guarantee"><b>Notre garantie / Our promise :</b> vous pouvez modifier ou annuler vos dons en tout temps. <span class="en">You may change or cancel at any time.</span> 514-726-3908 · hope@ashmeadfdn.org</p>
    </div>
  </section>

  <section class="panel tribute-panel">
    <p class="tribute-intro">Ce don est: <span class="sub">/ This gift is:</span><br>In Memoriam</p>
    <div class="name-line"></div>
    <p class="name-label">Nom de la personne décédée <span class="en">/ Name of the deceased</span></p>
    <p class="notify">Veuillez informer de mon geste: <span class="en">/ Please notify:</span></p>
    <div class="field">Nom <span class="en">/ Name</span>:<span class="line"></span></div>
    <div class="field">Adresse <span class="en">/ Address</span>:<span class="line"></span>App.:<span class="line short"></span></div>
    <div class="field">Ville <span class="en">/ City</span>:<span class="line"></span></div>
    <div class="field">Province:<span class="line short"></span>Code postal:<span class="line short"></span></div>
    <div class="flourish" role="img" aria-label="Gold ornamental rule"></div>

    <p class="tribute-head">In Honorarium</p>
    <div class="name-line"></div>
    <p class="name-label">Nom de la personne honorée <span class="en">/ Name of the honouree</span></p>
    <div class="field">Adresse <span class="en">/ Address</span>:<span class="line"></span>App.:<span class="line short"></span></div>
    <div class="field">Ville <span class="en">/ City</span>:<span class="line"></span></div>
    <div class="field">Province:<span class="line short"></span>Code postal:<span class="line short"></span></div>
    <div class="flourish" role="img" aria-label="Gold ornamental rule"></div>

    <p class="tribute-head">Ange gardien <span style="font-size:15px">/ Guardian Angel</span></p>
    <div class="name-line"></div>
    <p class="name-label">Nom de l'Ange gardien <span class="en">/ Name of the Guardian Angel</span></p>
    <div class="field">Département <span class="en">/ Department</span>:<span class="line"></span></div>
    <div class="flourish" role="img" aria-label="Gold ornamental rule"></div>

    <p class="anon"><span class="box"></span><span>Veuillez respecter mon souhait de rester anonyme.<br><span class="en">I wish to remain anonymous.</span></span></p>
    <div class="lang">Correspondance:
      <span class="check"><span class="box"></span>français</span>
      <span class="check"><span class="box"></span>anglais / English</span>
    </div>
  </section>

</main>
</body>
</html>
```